Navigate the Underground Car Park to 7K3R Vet Clinic

Eye-catching signage for Underground Carpark.
We want to help new Clients, or those with bad senses of direction, to the correct Lift Lobby.
We want to be able to say 'Just follow the signs'.

It can be confusing and many other business have utilised some of the pillars in the carpark to guide their customers to the right place.

People don't want to walk far with sick animals so it is important they get to the right Lift Lobby.
Updates

We are thinking instead of 'Just Follow the Signs,We would like to try:'Looking for us?' (Large Text)'Follow the Signs (much smaller Text)Also, it is very useful to see the proposed sign dropped on to the photo of the car park pillars I included.Many thanks Added Friday, June 16, 2017

Target Market(s)

Customers, coming for the 1st time, trying to navigate the Underground CarPark towards the appropriate Lift lobby

Industry/Entity Type

Veterinary

Font styles to use
Serif

Colors
f78f20
00a990
0455a3

Requirements
Must have
• Logo.
• Bright. Clear. Not too cluttered.
• Warmth. Humour. Approachable.
• Please include: Building 4, Mezzanine Level
Nice to have
• Please look at our FB pages and Instagram page @7k3rvetclinic for a good feel of who we are.
• Some level of style or image continuity with the Pet Tips Poster (see attached file)
Should not have
• Not have a medical feel

```html
<!DOCTYPE html>
<html lang="en">
<head>
<meta charset="utf-8">
<title>Looking For Us? – 7K3R Vet Clinic Car Park Sign</title>
<link rel="stylesheet" href="https://fonts.googleapis.com/css2?family=Fredoka:wght@400;500;600;700&display=swap">
<style>
  :root {
    --orange: #f78f20;
    --teal: #00a990;
    --blue: #0455a3;
    --white: #ffffff;
    --page-line: #555555;
    --pattern-peach: #f6e6d3;
    --pattern-mint: #e3efeb;
    --dog-tan: #c9a27a;
    --dog-light: #ede3d6;
  }
  * { margin: 0; padding: 0; box-sizing: border-box; }
  html, body {
    width: 1200px; height: 1199px; overflow: hidden;
    background: var(--white);
    font-family: "Fredoka", "Arial Rounded MT Bold", sans-serif;
  }
  .page {
    position: absolute; left: 207px; top: 43px;
    width: 787px; height: 1115px;
    border: 1px solid var(--page-line);
    background: var(--white);
  }
  .sign {
    position: absolute; left: 236px; top: 79px;
    width: 726px; height: 1046px;
    border: 5px solid var(--orange);
    border-radius: 14px;
    overflow: hidden;
    background: var(--white);
  }
  .sign__pattern {
    position: absolute; inset: 0 0 190px 0;
    background: linear-gradient(135deg, var(--pattern-peach) 0%, var(--pattern-mint) 50%, var(--pattern-peach) 100%);
    opacity: 0.55;
  }
  .headline {
    position: absolute; left: 0; right: 0; top: 52px;
    text-align: center; color: var(--blue);
    font-weight: 700; font-size: 118px; line-height: 124px;
    letter-spacing: 2px; text-transform: uppercase;
  }
  .tagline {
    position: absolute; left: 0; right: 0; top: 305px;
    display: flex; justify-content: center; align-items: center; gap: 14px;
    color: var(--blue); font-weight: 400; font-size: 31px;
    letter-spacing: 1.5px; text-transform: uppercase;
  }
  .tagline__paw {
    width: 44px; height: 44px; border-radius: 50%;
    background: var(--teal); border: 3px solid var(--white);
    box-shadow: 0 0 0 1px var(--pattern-mint);
  }
  .dog-photo {
    position: absolute; left: 265px; top: 400px;
    width: 456px; height: 455px;
    border-radius: 52% 40% 0 0 / 38% 30% 0 0;
    background: radial-gradient(ellipse at 60% 35%, var(--dog-tan) 0%, #b88a5f 45%, var(--dog-light) 85%);
  }
  .badge {
    position: absolute; left: 29px; top: 430px;
    width: 362px; height: 362px; overflow: visible;
  }
  .badge__ring-text { font-family: "Fredoka", sans-serif; font-weight: 600; fill: var(--teal); }
  .badge__address text {
    font-family: "Fredoka", sans-serif; font-weight: 500;
    fill: var(--white); font-size: 20px;
  }
  .contact-band {
    position: absolute; left: 0; right: 0; bottom: 0; height: 191px;
    background: var(--orange); color: var(--white);
  }
  .brand-box {
    position: absolute; left: 12px; top: 12px; width: 236px; height: 162px;
    background: var(--white);
    display: flex; align-items: center; justify-content: center; gap: 10px;
  }
  .brand-box__mark { width: 22px; height: 22px; border-radius: 50%; background: var(--orange); }
  .brand-box__name { color: var(--orange); font-weight: 500; font-size: 22px; }
  .contact-social { position: absolute; left: 271px; top: 22px; }
  .contact-social h2 {
    font-weight: 500; font-size: 25px; letter-spacing: 1.5px;
    text-transform: uppercase; margin-bottom: 10px;
  }
  .contact-line {
    display: flex; align-items: center; gap: 8px;
    font-size: 17px; font-weight: 400; height: 34px;
  }
  .contact-line__dot { width: 20px; height: 20px; border-radius: 50%; background: var(--white); }
  .contact-direct { position: absolute; left: 522px; top: 26px; }
  .contact-direct .contact-line { font-weight: 500; font-size: 18px; letter-spacing: 0.5px; }
  .contact-line svg { width: 22px; height: 22px; }
</style>
</head>
<body>
  <div class="page"></div>
  <main class="sign">
    <div class="sign__pattern" role="img" aria-label="Soft repeating pattern of peach and mint dog silhouettes"></div>

    <h1 class="headline">Looking<br>for us?</h1>

    <p class="tagline">
      <span class="tagline__paw" role="img" aria-label="Teal paw print"></span>
      Follow the signs
      <span class="tagline__paw" role="img" aria-label="Teal paw print"></span>
    </p>

    <div class="dog-photo" role="img" aria-label="Photo of a smiling tan dog with one ear flopped up"></div>

    <svg class="badge" viewBox="0 0 362 362" role="img" aria-label="Open 7 days a week – Silver Bay Arcade, Building 4, Mezzanine level">
      <defs>
        <path id="arc-top" d="M 51,181 A 130 130 0 0 1 311,181"/>
        <path id="arc-bottom" d="M 23,181 A 158 158 0 0 0 339,181"/>
      </defs>
      <circle cx="181" cy="181" r="176" fill="var(--white)" fill-opacity="0.9" stroke="var(--teal)" stroke-width="6"/>
      <circle cx="181" cy="181" r="118" fill="none" stroke="var(--teal)" stroke-width="3"/>
      <circle cx="181" cy="181" r="106" fill="var(--teal)"/>
      <g transform="rotate(-22 181 181)">
        <text class="badge__ring-text" font-size="46" letter-spacing="3" text-anchor="middle"><textPath href="#arc-top" startOffset="50%">OPEN</textPath></text>
      </g>
      <g transform="rotate(-22 181 181)">
        <text class="badge__ring-text" font-size="40" letter-spacing="2" text-anchor="middle"><textPath href="#arc-bottom" startOffset="50%">7 DAYS A WEEK</textPath></text>
      </g>
      <g class="badge__address" text-anchor="middle" transform="rotate(-12 181 181)">
        <text x="181" y="133">Silver Bay</text>
        <text x="181" y="158">Arcade</text>
        <text x="181" y="183">Building 4</text>
        <text x="181" y="208">Mezzanine</text>
        <text x="181" y="233">level</text>
      </g>
    </svg>

    <footer class="contact-band">
      <div class="brand-box">
        <span class="brand-box__mark"></span>
        <span class="brand-box__name">7K3R Vet Clinic</span>
      </div>
      <div class="contact-social">
        <h2>Contact us</h2>
        <p class="contact-line"><span class="contact-line__dot"></span>@7k3rvetclinic</p>
        <p class="contact-line"><span class="contact-line__dot"></span>7K3RVetsTheBay</p>
        <p class="contact-line"><span class="contact-line__dot"></span>7k3rpawsvet</p>
      </div>
      <div class="contact-direct">
        <p class="contact-line">
          <svg viewBox="0 0 24 24"><path fill="var(--white)" d="M6.6 10.8a15.1 15.1 0 0 0 6.6 6.6l2.2-2.2a1 1 0 0 1 1-.25 11.4 11.4 0 0 0 3.6.57 1 1 0 0 1 1 1V20a1 1 0 0 1-1 1A17 17 0 0 1 3 4a1 1 0 0 1 1-1h3.5a1 1 0 0 1 1 1c0 1.25.2 2.45.57 3.57a1 1 0 0 1-.25 1z"/></svg>
          800-7K3R-VET
        </p>
        <p class="contact-line">
          <svg viewBox="0 0 24 24"><path fill="var(--white)" d="M6.6 10.8a15.1 15.1 0 0 0 6.6 6.6l2.2-2.2a1 1 0 0 1 1-.25 11.4 11.4 0 0 0 3.6.57 1 1 0 0 1 1 1V20a1 1 0 0 1-1 1A17 17 0 0 1 3 4a1 1 0 0 1 1-1h3.5a1 1 0 0 1 1 1c0 1.25.2 2.45.57 3.57a1 1 0 0 1-.25 1z"/></svg>
          04 555 0193
        </p>
        <p class="contact-line">info@7k3rvet.example</p>
        <p class="contact-line">www.7k3rvet.example</p>
      </div>
    </footer>
  </main>
</body>
</html>
```